Web design for insurance consultant. Target clients are (re)insurers, insurtech firms and vendor...

Need a crisp, modern website which will talk briefly about the firm and its principal founder. And, details around services offered for 3 different target clients: (1) re/insurance companies, (2) insurtech and IoT firms, and (3) vendors such as claims adjusting firms and home inspection firms supporting insurers

Target Market(s)

C-suite leaders of insurance companies, reinsurance companies, insurtech firms looking to innovate property insurance, and vendors selling to these insurance companies. Focus is property insurance in coastal, catastrophe-exposed regions of the US.

Coding

Coded - Design and coding required

Number of Pages Required

5+ page

Other font styles liked:
• not sure of font wanted - classic, but modern

Colors
0792cd
00a990

Requirements
Must have
• First box should use the attached "light bulb storm" picture as background.
• one change overall - remove "Get a quote" button - we do not sell to consumers, it's strictly B2B.
• For the 3 segments, use the pictures below. I could not find one I liked for "TPAs/Vendors", so welcome your suggestions.
• Want quotes in the boxes of each of the 3 market segments.
• Button on each of the 3 market segments would lead to content (not yet finished) that will explain in more detail the services to be provided to them.
Should not have
• don't want google maps or others showing location of business (waste of space, in my opinion)

```html
<!DOCTYPE html>
<html lang="en">
<head>
<meta charset="utf-8">
<title>Halden Advisory – Insurance Consulting</title>
<link rel="stylesheet" href="https://fonts.googleapis.com/css2?family=Rajdhani:wght@500;600;700&family=Lato:wght@300;400;700&display=swap">
<style>
:root{
  --blue:#1a5d93;
  --blue-dark:#164f7e;
  --blue-box:#1f73b8;
  --green:#6aa515;
  --green-bright:#7cbf1a;
  --ink:#222;
  --muted:#555;
  --grey-bg:#f3f3f3;
  --line:#e3e3e3;
  --black:#0b0b0b;
  --white:#fff;
}
*{box-sizing:border-box;margin:0;padding:0}
html,body{width:1200px;height:3303px;overflow:hidden}
body{position:relative;font-family:"Lato",sans-serif;color:var(--ink);background:var(--white)}
.abs{position:absolute}
.head{font-family:"Rajdhani",sans-serif;font-weight:700}
.title{font-family:"Rajdhani",sans-serif;font-weight:700;font-size:40px;line-height:1;color:var(--blue)}
.title span{color:var(--green)}
.center{text-align:center;left:0;width:1200px}

/* hero */
.hero{left:0;top:0;width:1200px;height:562px;background:linear-gradient(180deg,#3a3a3a 0%,#5a5a5a 30%,#4a4a4a 65%,#2a2a2a 100%)}
.hero-shade{left:0;top:0;width:1200px;height:562px;background:linear-gradient(90deg,rgba(0,0,0,.45),rgba(0,0,0,.1) 50%,rgba(0,0,0,.45))}
.brand{left:176px;top:13px;height:62px;display:flex;align-items:center;gap:8px;color:var(--white);font-family:"Rajdhani",sans-serif;font-weight:700;font-size:26px}
.brand i{width:54px;height:54px;border-radius:50%;background:var(--white);display:block}
.nav{top:28px;right:162px;display:flex;gap:30px;font-family:"Rajdhani",sans-serif;font-weight:700;font-size:14px;color:var(--white)}
.slides{left:108px;top:216px;font-family:"Rajdhani",sans-serif;font-size:15px;color:var(--green-bright);line-height:28px}
.slides .on{color:var(--white)}
.slides .bar{width:1px;height:18px;background:var(--white);margin:2px 0 2px 6px}
.hero-title{top:192px;font-size:60px;color:var(--green-bright)}
.hero-sub{top:260px;font-size:23px;color:var(--white);font-family:"Lato",sans-serif}
.btn-blue{background:var(--blue);color:var(--white);font-family:"Rajdhani",sans-serif;font-weight:700;font-size:17px;display:flex;align-items:center;justify-content:center}

/* segments */
.seg{color:var(--white);text-align:center;padding:0 18px}
.seg h3{font-family:"Rajdhani",sans-serif;font-weight:700;font-size:17px;margin:10px 0 10px}
.seg p{font-size:11.5px;line-height:17px}
.seg svg{display:block;margin:0 auto}

/* about */
.about-text{left:161px;top:872px;width:430px;font-size:11.5px;line-height:17px;color:var(--muted)}
.about-text p+p{margin-top:17px}
.video{left:609px;top:819px;width:428px;height:260px;background:linear-gradient(135deg,#6b6b6b,#3b3b3b 60%,#2b2b2b)}

/* news */
.band-grey{left:0;width:1200px;background:var(--grey-bg)}
.card{background:var(--white);border:1px solid var(--line)}
.news-img{position:absolute;left:0;top:0;width:114px;height:100%}
.news-body{position:absolute;left:122px;top:6px;right:8px}
.news-body h4,.blog-body h4{font-family:"Lato",sans-serif;font-weight:700;font-size:11.5px;color:var(--blue);margin-bottom:4px}
.news-body p{font-size:10px;line-height:15px;color:var(--muted)}
.news-body a{display:block;font-size:10px;font-weight:700;color:var(--blue);margin-top:6px}

/* contact band */
.contact{left:0;top:1590px;width:1200px;height:339px;background:linear-gradient(135deg,#1f5c8c,#2f77ad 55%,#1d5a8c)}
.contact-q{top:1656px;font-family:"Rajdhani",sans-serif;font-weight:700;font-size:35px;line-height:46px;color:var(--white)}
.call{top:1793px;left:0;width:1200px;display:flex;justify-content:center;align-items:center;gap:18px;color:var(--white)}
.call .lbl{font-family:"Rajdhani",sans-serif;font-weight:500;font-size:28px;letter-spacing:1px}
.call .num{font-family:"Rajdhani",sans-serif;font-weight:700;font-size:42px}

/* testimonials */
.testi-photo{position:absolute;left:14px;top:14px;width:121px;height:120px}
.testi-body{position:absolute;left:150px;top:12px;right:12px}
.testi-body h5{font-size:10.5px;font-weight:700;color:var(--blue);margin-bottom:8px}
.testi-body p{font-size:11px;line-height:17px;color:var(--muted)}

/* blog */
.blog-img{position:absolute;left:0;top:0;width:100%;height:150px}
.blog-body{position:absolute;left:10px;top:164px;right:10px}
.blog-body p{font-size:10.5px;line-height:16px;color:var(--muted)}
.readmore{position:absolute;left:10px;top:271px;width:68px;height:24px;border:1px solid var(--green);font-size:8.5px;font-weight:700;color:var(--ink);display:flex;align-items:center;justify-content:center}
.blog-foot{position:absolute;left:0;bottom:0;width:100%;height:47px;background:var(--green)}

/* newsletter */
.newsletter{left:0;top:2874px;width:1200px;height:114px;background:var(--green)}
.nl-title{left:161px;top:2910px;font-size:40px;color:var(--white)}
.nl-input{left:535px;top:2909px;width:339px;height:44px;background:var(--white);font-size:11px;color:#666;padding:0 14px;display:flex;align-items:center}
.nl-btn{left:874px;top:2909px;width:148px;height:44px;background:var(--black);color:var(--white);font-family:"Rajdhani",sans-serif;font-weight:700;font-size:15px;display:flex;align-items:center;justify-content:center}

/* footer */
.footer{left:0;top:2988px;width:1200px;height:315px;background:var(--black);color:var(--white)}
.f-head{font-family:"Rajdhani",sans-serif;font-weight:700;font-size:16px;color:var(--green-bright)}
.f-text{font-size:11.5px;line-height:18px;color:#ddd}
.f-list li{list-style:none;font-size:11.5px;line-height:24px;color:#ddd;display:flex;align-items:center;gap:10px}
.f-list li::before{content:"";width:5px;height:5px;border-radius:50%;background:var(--green-bright)}
.info-row{display:flex;gap:16px;align-items:flex-start;font-size:11.5px;line-height:18px;color:#ddd}
</style>
</head>
<body>

<!-- hero -->
<div class="abs hero" role="img" aria-label="Photo of a business team in dark suits standing in an office"></div>
<div class="abs hero-shade"></div>
<div class="abs brand"><i></i>Halden Advisory</div>
<nav class="abs nav"><span>Home</span><span>About Us</span><span>Services</span><span>News</span><span>Contact Us</span></nav>
<div class="abs slides"><div>01</div><div>02</div><div class="bar"></div><div class="on">03</div><div>04</div></div>
<h1 class="abs center head hero-title">Need Solution for Insurance</h1>
<p class="abs center hero-sub">Visit Now The Halden Advisory</p>
<div class="abs btn-blue" style="left:537px;top:310px;width:126px;height:42px">CONTACT US</div>

<!-- segments -->
<div class="abs seg" style="left:161px;top:500px;width:290px;height:240px;background:var(--blue-box);padding-top:26px">
  <svg width="60" height="40" viewBox="0 0 60 40" fill="none" stroke="#fff" stroke-width="2"><circle cx="30" cy="12" r="7"/><path d="M17 36c0-8 6-13 13-13s13 5 13 13"/><circle cx="12" cy="16" r="5"/><path d="M2 34c0-6 4-9 10-9"/><circle cx="48" cy="16" r="5"/><path d="M58 34c0-6-4-9-10-9"/></svg>
  <h3>(Re)Insurers</h3>
  <p>“Halden has a unique skill set in property cat that helped us refine our approach, particularly in the challenging Florida market.He was instrumental to us in distilling down our business plan…</p>
</div>
<div class="abs seg" style="left:454px;top:484px;width:292px;height:276px;background:var(--green-bright);padding-top:44px">
  <svg width="56" height="56" viewBox="0 0 56 56" fill="none" stroke="#fff" stroke-width="2"><circle cx="28" cy="28" r="10"/><circle cx="28" cy="28" r="4"/><path d="M28 8v8M28 40v8M8 28h8M40 28h8M14 14l6 6M36 36l6 6M42 14l-6 6M20 36l-6 6"/></svg>
  <h3>Insurtech / IoT</h3>
  <p>“We didn’t realize how hard insurance is. Tom’s operational insights and suggestions across the organization (i.e., from submission/bind through to claims handling) accelerated our launch and build-out by a number of months.</p>
</div>
<div class="abs seg" style="left:749px;top:500px;width:288px;height:240px;background:var(--blue-box);padding-top:24px">
  <svg width="48" height="52" viewBox="0 0 48 52" fill="none" stroke="#fff" stroke-width="2"><path d="M24 3l18 7v14c0 13-8 21-18 25C14 45 6 37 6 24V10z"/><path d="M16 26l6 6 11-12"/></svg>
  <h3>Vendors and TPAs</h3>
  <p>“Halden knows everybody in this space. As important as his connections were to us, he also provided huge value to us in preparing and responding to RFPs. He’s expensive, but worth every penny!</p>
</div>

<!-- about -->
<h2 class="abs title" style="left:161px;top:821px">About <span>Us</span></h2>
<div class="abs about-text">
  <p>Lorem Ipsum is simply dummy text of the printing and typesetting industry. Lorem Ipsum has been the industry's standard dummy text ever since the 1500s, when an unknown printer took a galley of type and scrambled it to make a type specimen book.</p>
  <p>It has survived not only five centuries, but also the leap into electronic typesetting, remaining essentially unchanged.</p>
</div>
<div class="abs btn-blue" style="left:161px;top:1033px;width:92px;height:37px;font-size:12px">KNOW MORE</div>
<div class="abs video" role="img" aria-label="Video still of consultants in a meeting at a laptop"></div>
<svg class="abs" style="left:785px;top:913px" width="72" height="72" viewBox="0 0 72 72"><circle cx="36" cy="36" r="35" fill="#4f9a18" opacity=".5"/><circle cx="36" cy="36" r="26" fill="#6aa515"/><path d="M30 25l15 11-15 11z" fill="#fff"/></svg>

<!-- news -->
<div class="abs band-grey" style="top:1140px;height:450px"></div>
<h2 class="abs title" style="left:161px;top:1195px">Latest <span>News</span></h2>

<div class="abs card" style="left:161px;top:1262px;width:429px;height:119px"><div class="news-img" role="img" aria-label="Photo of a smiling professional at a desk" style="background:linear-gradient(135deg,#d8dfe4,#9aa9b4)"></div><div class="news-body"><h4>Lorem Ipsum is simply dummy text of the printing</h4><p>Lorem Ipsum is simply dummy text of the printing and typesetting industry. Lorem Ipsum has been the industry's standard dummy text ever since the 1500s,</p><a>Read More</a></div></div>
<div class="abs card" style="left:609px;top:1262px;width:428px;height:119px"><div class="news-img" role="img" aria-label="Photo of a team meeting in an office" style="background:linear-gradient(135deg,#b9b2a6,#5f5a54)"></div><div class="news-body"><h4>Lorem Ipsum is simply dummy text of the printing</h4><p>Lorem Ipsum is simply dummy text of the printing and typesetting industry. Lorem Ipsum has been the industry's standard dummy text ever since the 1500s,</p><a>Read More</a></div></div>
<div class="abs card" style="left:161px;top:1396px;width:429px;height:117px"><div class="news-img" role="img" aria-label="Photo of colleagues reviewing documents" style="background:linear-gradient(135deg,#e6dccf,#a89580)"></div><div class="news-body"><h4>Lorem Ipsum is simply dummy text of the printing</h4><p>Lorem Ipsum is simply dummy text of the printing and typesetting industry. Lorem Ipsum has been the industry's standard dummy text ever since the 1500s,</p><a>Read More</a></div></div>
<div class="abs card" style="left:609px;top:1396px;width:428px;height:117px"><div class="news-img" role="img" aria-label="Photo of a group discussion around a table" style="background:linear-gradient(135deg,#8a8e96,#3e4149)"></div><div class="news-body"><h4>Lorem Ipsum is simply dummy text of the printing</h4><p>Lorem Ipsum is simply dummy text of the printing and typesetting industry. Lorem Ipsum has been the industry's standard dummy text ever since the 1500s,</p><a>Read More</a></div></div>

<!-- contact band -->
<div class="abs contact" role="img" aria-label="Blue tinted photo of a desk with laptop and paperwork"></div>
<p class="abs center contact-q">If you have any questions about our company please<br>do not hesitate to contact us.</p>
<div class="abs call">
  <span class="lbl">CALL US ON</span>
  <svg width="54" height="54" viewBox="0 0 54 54" fill="none"><circle cx="27" cy="27" r="25" stroke="#7cbf1a" stroke-width="2"/><path d="M19 16c2-1 4 3 5 5s-2 3-1 5 4 5 6 6 3-3 5-1 5 3 4 5-4 4-7 3-13-8-14-14 0-8 2-9z" fill="#7cbf1a"/></svg>
  <span class="num">+91-000-000-0000</span>
</div>

<!-- testimonials -->
<h2 class="abs title center" style="top:2002px">Our <span>Testimonials</span></h2>
<div class="abs card" style="left:161px;top:2068px;width:429px;height:147px"><div class="testi-photo" role="img" aria-label="Portrait photo of a client" style="background:linear-gradient(135deg,#7b5a4a,#2d2420)"></div><div class="testi-body"><h5>• CLIENT NAME</h5><p>Lorem Ipsum is simply dummy text of the printing and typesetting industry. Lorem Ipsum has been the industry's standard dummy text ever since the 1500s, when an unknown printer took a galley of type and scrambled it to make a type specimen</p></div></div>
<div class="abs card" style="left:609px;top:2068px;width:428px;height:147px"><div class="testi-photo" role="img" aria-label="Portrait photo of a client" style="background:linear-gradient(135deg,#9fb3c8,#2f3e56)"></div><div class="testi-body"><h5>• CLIENT NAME</h5><p>Lorem Ipsum is simply dummy text of the printing and typesetting industry. Lorem Ipsum has been the industry's standard dummy text ever since the 1500s, when an unknown printer took a galley of type and scrambled it to make a type specimen</p></div></div>
<svg class="abs" style="left:560px;top:2238px" width="80" height="30" viewBox="0 0 80 30"><circle cx="15" cy="15" r="14" fill="#1a5d93"/><path d="M21 15H10M14 10l-5 5 5 5" stroke="#fff" stroke-width="2.5" fill="none"/><circle cx="63" cy="15" r="14" fill="#1a5d93"/><path d="M57 15h11M64 10l5 5-5 5" stroke="#fff" stroke-width="2.5" fill="none"/></svg>

<!-- blog -->
<div class="abs band-grey" style="top:2312px;height:562px"></div>
<h2 class="abs title center" style="top:2374px">Our <span>Blog</span></h2>
<div class="abs card" style="left:161px;top:2462px;width:280px;height:324px;border:none"><div class="blog-img" role="img" aria-label="Photo of a business meeting around a table" style="background:linear-gradient(135deg,#a79c92,#3e3a38)"></div><div class="blog-body"><h4 style="color:var(--ink)">Lorem Ipsum is simply dummy text of the.</h4><p>Lorem Ipsum is simply dummy text of the printing and typesetting industry. Lorem Ipsum has been the industry's standard dummy text ever since the 1500s</p></div><div class="readmore">READMORE</div></div>
<div class="abs card" style="left:462px;top:2462px;width:278px;height:324px;border:none"><div class="blog-img" role="img" aria-label="Green tinted photo of financial charts on a desk" style="background:linear-gradient(135deg,#a9d35a,#6aa515)"></div><div class="blog-body"><h4 style="color:var(--ink)">Lorem Ipsum is simply dummy text of the.</h4><p>Lorem Ipsum is simply dummy text of the printing and typesetting industry. Lorem Ipsum has been the industry's standard dummy text ever since the 1500s</p></div><div class="blog-foot"></div><div class="readmore" style="top:288px;border-color:#fff;color:#fff">READMORE</div>
  <svg class="abs" style="left:132px;top:299px" width="130" height="24" viewBox="0 0 130 24"><circle cx="12" cy="12" r="6" fill="#fff"/><circle cx="46" cy="12" r="6" fill="#fff"/><circle cx="80" cy="12" r="6" fill="#fff"/><circle cx="114" cy="12" r="6" fill="#fff"/></svg></div>
<div class="abs card" style="left:762px;top:2462px;width:275px;height:324px;border:none"><div class="blog-img" role="img" aria-label="Photo of a team working together on laptops" style="background:linear-gradient(135deg,#7f8aa0,#3a3f55)"></div><div class="blog-body"><h4 style="color:var(--ink)">Lorem Ipsum is simply dummy text of the.</h4><p>Lorem Ipsum is simply dummy text of the printing and typesetting industry. Lorem Ipsum has been the industry's standard dummy text ever since the 1500s</p></div><div class="readmore">READMORE</div></div>

<!-- newsletter -->
<div class="abs newsletter"></div>
<h2 class="abs head nl-title">OUR NEWSLETTER</h2>
<div class="abs nl-input">Enter your email here...*</div>
<div class="abs nl-btn">SUBSCRIBE</div>

<!-- footer -->
<footer class="abs footer">
  <div class="abs" style="left:161px;top:50px;display:flex;align-items:center;gap:8px;font-family:'Rajdhani',sans-serif;font-weight:700;font-size:24px;color:#fff"><i style="display:block;width:46px;height:46px;border-radius:50%;background:#fff"></i>Halden Advisory</div>
  <p class="abs f-text" style="left:161px;top:122px;width:210px">Lorem Ipsum is simply dummy text of the printing and typesetting industry. Lorem Ipsum has been the industry's.</p>

  <h4 class="abs f-head" style="left:388px;top:48px">Our Info</h4>
  <div class="abs" style="left:395px;top:92px;display:flex;flex-direction:column;gap:22px">
    <div class="info-row"><svg width="14" height="14" viewBox="0 0 14 14"><path d="M3 1c1 0 2 2 2 3s-1 1-1 2 2 3 3 3 1-1 2-1 3 1 3 2-1 3-3 3S1 9 1 4c0-2 1-3 2-3z" fill="#7cbf1a"/></svg><span>+91-000-000-0000</span></div>
    <div class="info-row"><svg width="14" height="14" viewBox="0 0 14 14"><rect x="1" y="3" width="12" height="9" fill="#7cbf1a"/><path d="M1 3l6 5 6-5" stroke="#000" fill="none"/></svg><span>info@haldenadvisory.com</span></div>
    <div class="info-row"><svg width="14" height="16" viewBox="0 0 14 16"><path d="M7 1a5 5 0 015 5c0 4-5 9-5 9S2 10 2 6a5 5 0 015-5z" fill="#7cbf1a"/><circle cx="7" cy="6" r="2" fill="#000"/></svg><span>31 Lorem Ipsum is simply<br>dummy text for printing.</span></div>
  </div>

  <h4 class="abs f-head" style="left:612px;top:48px">Sitemap</h4>
  <ul class="abs f-list" style="left:612px;top:94px"><li>Home</li><li>About us</li><li>Services</li><li>News</li><li>Contact us</li></ul>

  <h4 class="abs f-head" style="left:837px;top:48px">Follow Us On:</h4>
  <svg class="abs" style="left:837px;top:82px" width="130" height="32" viewBox="0 0 130 32"><circle cx="15" cy="16" r="14" fill="#6aa515"/><circle cx="49" cy="16" r="14" fill="#6aa515"/><circle cx="83" cy="16" r="14" fill="#6aa515"/><circle cx="117" cy="16" r="14" fill="#6aa515"/></svg>
  <div class="abs" style="left:837px;top:152px;width:200px;height:34px;border-radius:17px;background:#fff;color:var(--blue);font-size:11.5px;font-weight:700;display:flex;align-items:center;padding-left:20px">View The Map Directions
    <svg class="abs" style="right:2px;top:2px" width="30" height="30" viewBox="0 0 30 30"><circle cx="15" cy="15" r="15" fill="#6aa515"/><path d="M9 15h11M15 10l5 5-5 5" stroke="#fff" stroke-width="2.5" fill="none"/></svg></div>

  <div class="abs" style="left:161px;top:260px;width:876px;height:1px;background:#333"></div>
  <p class="abs center" style="top:282px;font-size:11px;color:#ddd">Copyright © 2019 <span style="color:var(--green-bright)">HALDEN ADVISORY</span> - All Rights Reserved.</p>
</footer>

</body>
</html>
```